Mixed Martial Arts Business Book Cover

Dorian Caskell Jr aka The Dojo Growth Mentor Presents

The name of my book is

"Our Studio Fortune Atlas"

tagline is

"The Anything Goes Manual For Growing Your Combat Gym Into A TRUE Enterprise"

I would like like my image incorporated some how

Target Market(s)

mixed martial arts and brazilian jiu jitsu school owners

Industry/Entity Type

Business

Requirements
Must have
• The image I provided incorporated some how (unless) yiou just think its stupid and wont work
Nice to have
• these guys own schools teach people in the QKT cage fighting so I'm not sure but the qkt cage fence ( a fence look) may be cool, or maybe not but i'm not opposedto seeing a design with a cage/fence also
• nice to have the image i provided if possible
Should not have
• should not have any images of random fighters

```html
<!DOCTYPE html>
<html lang="en">
<head>
<meta charset="UTF-8">
<title>Our Studio Fortune Atlas — Book Cover</title>
<link rel="stylesheet" href="https://fonts.googleapis.com/css2?family=Oswald:wght@600;700&family=Anton&display=swap">
<style>
  :root {
    --arena-deep: #08122a;
    --arena-mid: #1d3a74;
    --arena-light: #4f73b4;
    --spot-glow: #e4ecff;
    --ink-white: #ffffff;
    --ink-black: #000000;
    --chrome-hi: #f6f8fb;
    --chrome-mid: #a7afbd;
    --chrome-low: #4b5262;
    --chrome-edge: #1a1e26;
  }
  * { margin: 0; padding: 0; box-sizing: border-box; }
  html, body {
    width: 800px;
    height: 1200px;
    overflow: hidden;
    background: var(--arena-deep);
  }
  .cover {
    position: relative;
    width: 800px;
    height: 1200px;
    overflow: hidden;
  }
  .arena-photo {
    position: absolute;
    inset: 0;
    display: block;
  }
  .presenter {
    position: absolute;
    top: 72px;
    left: 0;
    right: 0;
    text-align: center;
    font-family: "Oswald", sans-serif;
    font-weight: 700;
    font-size: 31px;
    line-height: 1.2;
    letter-spacing: 0.3px;
    color: var(--ink-white);
    text-transform: uppercase;
    text-shadow: 0 2px 5px rgba(0,0,0,0.7);
  }
  .presenter em { font-style: italic; }
  .book-title {
    position: absolute;
    top: 364px;
    left: 0;
    right: 0;
    text-align: center;
    font-family: "Anton", sans-serif;
    font-weight: 400;
    font-size: 136px;
    line-height: 128px;
    text-transform: uppercase;
    letter-spacing: 3px;
  }
  .book-title span {
    display: block;
    background: linear-gradient(180deg, var(--chrome-hi) 0%, var(--chrome-mid) 46%, var(--chrome-low) 54%, var(--chrome-hi) 100%);
    -webkit-background-clip: text;
    background-clip: text;
    color: transparent;
    -webkit-text-stroke: 2px var(--chrome-edge);
    filter: drop-shadow(0 5px 6px rgba(0,0,0,0.65));
  }
  .tagline {
    position: absolute;
    top: 980px;
    left: 0;
    right: 0;
    text-align: center;
    font-family: "Oswald", sans-serif;
    font-weight: 700;
    font-size: 33px;
    line-height: 1;
    color: var(--ink-white);
    text-transform: uppercase;
  }
  .tagline span {
    display: inline-block;
    background: var(--ink-black);
    padding: 5px 10px 6px;
    margin-bottom: 2px;
  }
</style>
</head>
<body>
  <main class="cover">
    <svg class="arena-photo" width="800" height="1200" viewBox="0 0 800 1200" role="img" aria-label="Client photo: empty fight arena under a row of bright spotlights, seen through a chain-link cage fence with glass shattering outward">
      <defs>
        <radialGradient id="arenaBody" cx="50%" cy="55%" r="70%">
          <stop offset="0%" stop-color="#4f73b4"/>
          <stop offset="50%" stop-color="#1d3a74"/>
          <stop offset="100%" stop-color="#08122a"/>
        </radialGradient>
        <radialGradient id="spotRow" cx="50%" cy="50%" r="50%">
          <stop offset="0%" stop-color="#e4ecff" stop-opacity="0.75"/>
          <stop offset="100%" stop-color="#e4ecff" stop-opacity="0"/>
        </radialGradient>
      </defs>
      <rect width="800" height="1200" fill="url(#arenaBody)"/>
      <ellipse cx="400" cy="200" rx="440" ry="120" fill="url(#spotRow)"/>
    </svg>

    <p class="presenter">Dorian Caskell Jr aka the<br>Dojo Growth Mentor <em>Presents</em></p>

    <h1 class="book-title">
      <span>Our Studio</span>
      <span>Fortune</span>
      <span>Atlas</span>
    </h1>

    <p class="tagline">
      <span>The Anything Goes Manual</span><br>
      <span>For Growing Your Combat Gym</span><br>
      <span>Into A True Enterprise</span>
    </p>
  </main>
</body>
</html>
```